Business card & Letter head for accounting firm
TRW Ledger Partners, LLC
Professional
Ravi T. Belmonde, CPA CFE
Partner
42 Harlow Street West
Edison, NJ 08817
rbelmonde@trwlpcpa.com
www.trwlpcpa.com
Licensed CPA in NY & NJ
Would like to see the logo on the front of the card and contact information on the back of card
On the back would like to see the new scan able contact information if possible
vector logo

```html
<!DOCTYPE html>
<html lang="en">
<head>
<meta charset="utf-8">
<title>TRW Ledger Partners, LLC — Stationery</title>
<link href="https://fonts.googleapis.com/css2?family=Open+Sans:wght@400;700&display=swap" rel="stylesheet">
<style>
  :root {
    --page: #ffffff;
    --frame: #d4d4d4;
    --paper: #ffffff;
    --brand-blue: #3d5fa8;
    --brand-green: #8cc63f;
    --ink: #666666;
    --shadow: rgba(0,0,0,0.22);
  }
  * { box-sizing: border-box; margin: 0; padding: 0; }
  html, body { width: 1200px; height: 681px; overflow: hidden; background: var(--page); }
  body { font-family: "Open Sans", Arial, sans-serif; color: var(--ink); position: relative; }

  .presentation-frame {
    position: absolute; left: 24px; top: 29px; width: 1152px; height: 624px;
    border: 1px solid var(--frame); background: var(--page);
  }
  .sheet {
    position: absolute; background: var(--paper);
    box-shadow: 2px 3px 6px var(--shadow);
    border: 1px solid #e2e2e2;
  }

  .wordmark { display: flex; align-items: center; gap: 4px; }
  .wordmark-square { background: var(--brand-green); flex: none; }
  .wordmark-name { font-weight: 700; color: var(--brand-blue); letter-spacing: 1px; line-height: 1; }

  .divider { position: absolute; width: 2px; background: var(--brand-green); }
  .contact-block { position: absolute; font-size: 6px; line-height: 1.4; color: var(--ink); }

  /* Envelope front */
  .envelope-front { left: 62px; top: 96px; width: 478px; height: 204px; }
  .envelope-front .wordmark { position: absolute; left: 12px; top: 20px; }
  .envelope-front .wordmark-square { width: 16px; height: 16px; }
  .envelope-front .wordmark-name { font-size: 24px; }
  .envelope-front .divider { left: 112px; top: 14px; height: 64px; }
  .envelope-front .contact-block { left: 122px; top: 15px; }

  /* Envelope back */
  .envelope-back { left: 62px; top: 324px; width: 478px; height: 223px; }
  .envelope-back .flap { position: absolute; left: 0; top: 0; width: 100%; height: 60px; }
  .envelope-back .wordmark { position: absolute; left: 50%; top: 74px; transform: translateX(-50%); }
  .envelope-back .wordmark-square { width: 18px; height: 18px; }
  .envelope-back .wordmark-name { font-size: 28px; }

  /* Letterhead */
  .letterhead { left: 619px; top: 48px; width: 336px; height: 581px; }
  .letterhead .wordmark { position: absolute; left: 18px; top: 34px; }
  .letterhead .wordmark-square { width: 16px; height: 16px; }
  .letterhead .wordmark-name { font-size: 26px; }
  .letterhead .divider { left: 110px; top: 24px; height: 62px; }
  .letterhead .contact-block { left: 120px; top: 24px; font-size: 6.5px; }

  /* Business cards */
  .card-front { left: 965px; top: 115px; width: 163px; height: 113px; }
  .card-front .wordmark { position: absolute; left: 50%; top: 50%; transform: translate(-50%, -50%); }
  .card-front .wordmark-square { width: 14px; height: 14px; }
  .card-front .wordmark-name { font-size: 22px; }

  .card-back { left: 965px; top: 247px; width: 163px; height: 113px; }
  .card-back .wordmark { position: absolute; left: 8px; top: 36px; }
  .card-back .wordmark-square { width: 9px; height: 9px; }
  .card-back .wordmark-name { font-size: 15px; }
  .card-back .divider { left: 62px; top: 16px; height: 72px; width: 1.5px; }
  .card-back .contact-block { left: 68px; top: 16px; font-size: 4.6px; line-height: 1.45; }
  .card-back .person-name { color: var(--brand-blue); font-weight: 700; }
  .card-back .person-title { margin-bottom: 4px; }
</style>
</head>
<body>
  <div class="presentation-frame"></div>

  <section class="sheet envelope-front" aria-label="Envelope front">
    <div class="wordmark"><span class="wordmark-square"></span><span class="wordmark-name">TRW</span></div>
    <div class="divider"></div>
    <address class="contact-block" style="font-style:normal">
      42 Harlow Street West<br>
      Edison, NJ 08817<br>
      Phone: (732) 555-0142<br>
      Cell: (732) 555-0187<br>
      Fax: (732) 555-0199<br>
      Email: rbelmonde@trwlpcpa.com<br>
      www.trwlpcpa.com
    </address>
  </section>

  <section class="sheet envelope-back" aria-label="Envelope back">
    <svg class="flap" viewBox="0 0 478 60" preserveAspectRatio="none" aria-hidden="true">
      <path d="M2 2 Q 20 40 60 44 L 418 44 Q 458 40 476 2" fill="none" stroke="#9a9a9a" stroke-width="1.2"/>
    </svg>
    <div class="wordmark"><span class="wordmark-square"></span><span class="wordmark-name">TRW</span></div>
  </section>

  <section class="sheet letterhead" aria-label="Letterhead">
    <div class="wordmark"><span class="wordmark-square"></span><span class="wordmark-name">TRW</span></div>
    <div class="divider"></div>
    <address class="contact-block" style="font-style:normal">
      42 Harlow Street West<br>
      Edison, NJ 08817<br>
      Phone: (732) 555-0142<br>
      Cell: (732) 555-0187<br>
      Fax: (732) 555-0199<br>
      Email: rbelmonde@trwlpcpa.com<br>
      www.trwlpcpa.com
    </address>
  </section>

  <section class="sheet card-front" aria-label="Business card front">
    <div class="wordmark"><span class="wordmark-square"></span><span class="wordmark-name">TRW</span></div>
  </section>

  <section class="sheet card-back" aria-label="Business card back">
    <div class="wordmark"><span class="wordmark-square"></span><span class="wordmark-name">TRW</span></div>
    <div class="divider"></div>
    <address class="contact-block" style="font-style:normal">
      <div class="person-name">Ravi T. Belmonde, CPA CFE</div>
      <div class="person-title">Partner</div>
      42 Harlow Street West<br>
      Edison, NJ 08817<br>
      Phone: (732) 555-0142<br>
      Cell: (732) 555-0187<br>
      Fax: (732) 555-0199<br>
      rbelmonde@trwlpcpa.com<br>
      www.trwlpcpa.com
    </address>
  </section>
</body>
</html>
```